依頼詳細
【仕様】
『資格完全攻略 突破 ケアワーカー ノート&ドリル 2014 基礎分野編』『資格完全攻略 突破 ケアワーカー ノート&ドリル 2014 応用分野編』は同じ仕様となります。
・B5(182 × 257 ㎜)
・背幅はおよそ20㎜です(修正有)。
・本文は横書ですので左綴じとなります。
・カバー(表1、表4、背表紙):4C(フルカラー)
・表紙(表1、表4、背表紙):1C
・扉:1C

※表紙・扉のデザインはカバーデザインに基づいたもので、「書名」「編者名」「社名」だけが入っているもので結構です。
記載項目
【デザインについて】
・同資格のための参考書・問題集・ワークブックは類書が数多くあり、なかなか差別化が図れないのが現状です。今回は、「資格受験用テキスト・問題集」によく見られるようなキャッチコピーが踊るデザインではなく、すっきりとした知的かつスマートなデザインを希望します。
・書籍の内容は堅いですが、読者が手に取りやすい親しみやすさも加味してください。
・『要点整理と演習集』のデザインにはとらわれませんし、イラスト等を加えていただいても結構です。
・タイトルの文字についてですが、「社会福祉士」「合格」「2013」「共通科目編」「専門科目編」が目に付くようにしてください。特に「社会福祉士」の文言については100級以上の大きさでお願いをします。
・2つの書籍でデザインに盛り込む内容(文字)が異なります。書名、編者名等のデザインに盛り込む内容(文字)は添付ファイルを参照してください。

その他、ご不明な点は、お気軽にお問い合わせください。
希望イメージ
シンプル 複雑
単色 カラフル
暗い 明るい
日常 高級
遊び心 厳粛
未来的 伝統的
女性的 男性的
希望する色
特になし
納品ファイル
• イラストレーター形式 (.ai)
補足説明
■ 選んだ理由

①従来の弊社の書籍とは違うやわらかいイメージ。
②他社の類書との差別化がはかれるデザイン。
③書籍の内容(テキスト・問題集)がもつ「堅い」イメージをやわらげてくれるデザイン。

■ 提案者全員のお礼・コメント

この度は多くのご提案ありがとうございました。
ご応募くださった皆様の提案はとてもバラエティに富み、素晴らしいものが多く迷いましたが、上記の理由により選定させていただきました。
それぞれの提案に社内では「他の書籍ならこのデザインがいい」といった声もきかれました。今回の書籍では惜しくも採用にいたらなかった提案も違う案件によっては十分に採用される可能性がありました。
今後もこのようなデザインをしていただきたい案件がございます。またの機会にも是非ご応募くださいますようお願いいたします。

```html
<!DOCTYPE html>
<html lang="ja">
<head>
<meta charset="utf-8">
<title>資格完全攻略 突破 ケアワーカー ノート&ドリル 2014 応用分野編</title>
<link href="https://fonts.googleapis.com/css2?family=Noto+Sans+JP:wght@400;500;700;900&display=swap" rel="stylesheet">
<style>
  :root{
    --teal:#1b8fb0;
    --teal-dark:#0f6f8c;
    --green:#7cbf2a;
    --pale:#dff1f7;
    --ink:#3a3a3a;
    --grey:#6b6b6b;
    --white:#ffffff;
  }
  *{margin:0;padding:0;box-sizing:border-box}
  html,body{width:849px;height:1200px;overflow:hidden;background:var(--white)}
  .cover{position:relative;width:849px;height:1200px;background:var(--white);font-family:"Noto Sans JP",sans-serif;color:var(--ink);overflow:hidden}
  .corner-tab{position:absolute;right:0;top:0}
  .title-band{position:absolute;left:0;top:250px;width:849px;height:420px;background:linear-gradient(90deg,rgba(223,241,247,0) 0%,var(--pale) 55%,#c7e6f1 100%)}
  .features{position:absolute;left:112px;top:40px;list-style:none}
  .features li{display:flex;align-items:center;gap:12px;font-size:25px;font-weight:700;color:var(--ink);margin-bottom:14px;letter-spacing:.5px}
  .features svg{flex:none}
  .pass-bubble{position:absolute;left:548px;top:220px}
  .pass-bubble span{position:absolute;left:0;top:0;width:110px;height:66px;display:flex;align-items:center;justify-content:center;font-size:34px;font-weight:900;color:var(--ink)}
  .series{position:absolute;left:140px;top:258px;font-size:40px;font-weight:500;color:var(--ink);letter-spacing:2px}
  .main-title{position:absolute;left:134px;top:300px;font-size:98px;font-weight:900;color:var(--teal);letter-spacing:2px;line-height:1.1}
  .sub-title{position:absolute;left:140px;top:420px;font-size:50px;font-weight:500;color:var(--grey);letter-spacing:1px}
  .sub-title b{color:var(--teal);font-weight:900}
  .year{position:absolute;left:136px;top:490px;font-size:82px;font-weight:900;color:var(--teal);line-height:1}
  .volume{position:absolute;left:126px;top:582px;padding:4px 18px;background:var(--teal);color:var(--white);font-size:44px;font-weight:900;letter-spacing:2px}
  .contents{position:absolute;left:536px;top:405px;width:216px;padding:12px 12px;background:var(--white);border:2px solid var(--teal)}
  .contents h3{font-size:14px;font-weight:700;color:var(--teal);margin-bottom:6px}
  .contents ul{list-style:none;font-size:12px;line-height:1.55;color:var(--ink)}
  .contents li::before{content:"■";color:var(--teal);margin-right:3px}
  .rule{position:absolute;left:112px;top:880px;width:640px;height:2px;background:var(--teal)}
  .notes{position:absolute;left:112px;top:895px;width:640px;font-size:19px;line-height:1.6;color:var(--ink)}
  .notes p{display:flex}
  .notes dt,.notes .label{flex:none;color:var(--teal);font-weight:900}
  .credits{position:absolute;left:112px;top:1040px;font-size:20px;line-height:1.5;color:var(--ink)}
  .credits .person{font-size:22px;font-weight:700}
  .publisher{position:absolute;right:96px;top:1105px;font-size:24px;font-weight:500;color:var(--ink)}
</style>
</head>
<body>
<div class="cover">
  <svg class="corner-tab" width="260" height="110" viewBox="0 0 260 110" aria-hidden="true">
    <polygon points="40,0 260,0 260,110 110,110" fill="var(--teal)"/>
    <polygon points="40,0 110,110 80,110" fill="var(--teal-dark)"/>
  </svg>

  <div class="title-band"></div>

  <ul class="features">
    <li><svg width="26" height="26" viewBox="0 0 26 26"><circle cx="13" cy="13" r="13" fill="var(--green)"/><path d="M7 13l4 4 8-9" stroke="#fff" stroke-width="3" fill="none" stroke-linecap="round" stroke-linejoin="round"/></svg>系統立てた記述で理解度アップ!</li>
    <li><svg width="26" height="26" viewBox="0 0 26 26"><circle cx="13" cy="13" r="13" fill="var(--green)"/><path d="M7 13l4 4 8-9" stroke="#fff" stroke-width="3" fill="none" stroke-linecap="round" stroke-linejoin="round"/></svg>効果的な学習をサポートする<br>合格力養成テキスト</li>
  </ul>

  <div class="pass-bubble">
    <svg width="110" height="86" viewBox="0 0 110 86" aria-hidden="true">
      <path d="M10 3h90a7 7 0 0 1 7 7v46a7 7 0 0 1-7 7H40l-16 18 2-18H10a7 7 0 0 1-7-7V10a7 7 0 0 1 7-7z" fill="#fff" stroke="var(--green)" stroke-width="4"/>
    </svg>
    <span>突破</span>
  </div>

  <div class="series">資格完全攻略</div>
  <h1 class="main-title">ケアワーカー</h1>
  <div class="sub-title">ノート<b>&amp;</b>ドリル</div>
  <div class="year">2014</div>
  <div class="volume">応用分野編</div>

  <div class="contents">
    <h3>応用分野編</h3>
    <ul>
      <li>社会調査の基礎</li>
      <li>相談援助の基盤と専門職</li>
      <li>相談援助の理論と方法</li>
      <li>福祉サービスの組織と経営</li>
      <li>高齢者に対する支援と介護保険制度</li>
      <li>児童や家庭に対する支援と制度</li>
      <li>就労支援サービス</li>
      <li>更生保護制度</li>
    </ul>
  </div>

  <div class="rule"></div>
  <div class="notes">
    <p><span class="label">スタディ:</span><span>学科の出題範囲をカバーし、合格圏内の6割以上を正答するための必修事項を精選してわかりやすく解説。</span></p>
    <p><span class="label">チェック:</span><span>合格のために必要となる必須の知識を確認するための一問一答(過去問題・オリジナル問題)を大項目ごとに収録。</span></p>
  </div>

  <div class="credits">
    <div class="person">森川 遥 監修</div>
    <div>ケアワーカー資格研究会 編集</div>
  </div>

  <div class="publisher">(株)あおば書房</div>
</div>
</body>
</html>
```